Bright Quest Appeal needs a brochure

I need an A4 - Two sided brochure design.
It's for a maths challenge fundraiser for primary schools throughout Australia.
It needs to be bright and fun with the pictures / files supplied,
Please use as many pics as you can, more the better...
Also keep Logos as transparent
See our website for an idea of what we do pls. brightquestappeal.example
Pls make it FUN ....NOT corporate..
so curves and colours rather than straight lines
The only headings that need to be ALL capitals is "FREE TO JOIN" & "FUNDRAISER" Other titles not all capitals pls
Please note: when putting in the pics of the games, pls put in order from game1-7 as they go in order of the school grade levels (Preschool to Grade 6). showing teachers how they become more difficult...in that order.
This brochure will be sent to schools.
Schools have admin open letters, we get about 2 - 3 seconds for admin to decide to keep or bin the brochure, so they need to see it's a fundraiser and "free to join" in those seconds.
cheers
- fun style maybe marker felt or comic sans but you choose any other you think works to make it fun

```html
<!DOCTYPE html>
<html lang="en">
<head>
<meta charset="utf-8">
<title>Bright Quest Appeal – Maths Challenge Fundraiser Brochure</title>
<link rel="stylesheet" href="https://fonts.googleapis.com/css2?family=Bubblegum+Sans&family=Open+Sans:wght@400;600;700&display=swap">
<style>
:root{
  --stage:#e9ebee;
  --paper:#f1f8fc;
  --paper-edge:#dcecf5;
  --red:#e3222f;
  --blue:#1f3a9c;
  --sky:#8fd0ec;
  --green:#7cbd2a;
  --orange:#f05a22;
  --purple:#7b2d8e;
  --gold:#d9a21b;
  --ink:#222a33;
  --muted:#3b4450;
  --game-deep:#0f1e5a;
}
*{box-sizing:border-box;margin:0;padding:0}
html,body{width:1200px;height:900px;overflow:hidden;background:var(--stage)}
body{position:relative;font-family:"Open Sans",sans-serif;color:var(--ink)}
.display{font-family:"Bubblegum Sans",cursive;font-weight:400}
.page{position:absolute;top:68px;width:540px;height:764px;overflow:hidden;
  background:linear-gradient(160deg,#ffffff 0%,var(--paper) 45%,var(--paper-edge) 100%);
  box-shadow:0 6px 18px rgba(0,0,0,.18)}
.page--front{left:40px}
.page--back{left:620px}
.abs{position:absolute}
.layer{position:absolute;inset:0}

/* front */
.title-maths{left:48px;top:30px;font-size:66px;line-height:1;letter-spacing:1px}
.title-challenge{left:52px;top:96px;font-size:42px;line-height:1}
.title-fundraiser{left:52px;top:140px;font-size:40px;line-height:1;color:var(--gold)}
.c-red{color:var(--red)}.c-blue{color:var(--blue)}.c-green{color:var(--green)}
.c-orange{color:var(--orange)}.c-purple{color:var(--purple)}.c-gold{color:var(--gold)}
.brand{right:18px;top:18px;width:150px;height:86px;border-radius:50%;background:#fff;
  border:4px solid var(--red);display:flex;align-items:center;justify-content:center;gap:6px;
  text-align:center;font-size:16px;line-height:1.05;color:var(--red)}
.brand-dot{width:12px;height:12px;border-radius:50%;background:var(--red);flex:none}
.tagline{left:40px;top:186px;width:350px;text-align:center;font-size:19px;line-height:1.2;color:var(--ink)}
.photo{position:absolute;border-radius:50%}
.photo--classroom{left:395px;top:155px;width:190px;height:190px;
  background:radial-gradient(circle at 40% 40%,#d9b59a,#8c6a58 60%,#4b5a6a)}
.photo--cheer{left:98px;top:313px;width:104px;height:104px;
  background:radial-gradient(circle at 50% 40%,#e9d6c6,#c7a38e 60%,#8a7c76)}
.challenge-badge{left:205px;top:240px;width:160px;height:160px;border-radius:50%;background:var(--red);
  color:#fff;text-align:center;padding-top:32px}
.challenge-badge .big{font-size:29px;line-height:1}
.challenge-badge .mid{font-size:16px;line-height:1.1}
.challenge-badge .small{font-size:8.5px;line-height:1.3;margin:6px auto 0;width:116px}
.free-badge{left:14px;top:352px;width:80px;height:80px;border-radius:50%;background:var(--orange);
  color:#fff;text-align:center;font-size:20px;line-height:.95;padding-top:16px}
.fun-head{left:30px;top:478px;line-height:1.05}
.fun-head .l1{font-size:16px;color:var(--purple)}
.fun-head .l2{font-size:19px;color:var(--red)}
.ticks{list-style:none;font-size:10px;line-height:1.4;color:var(--muted)}
.ticks li{position:relative;padding-left:24px;margin-bottom:10px}
.ticks svg{position:absolute;left:0;top:0;width:15px;height:13px}
.ticks--left{left:30px;top:526px;width:228px}
.ticks--right{left:278px;top:522px;width:250px}
.effortless{left:260px;top:428px;width:280px;text-align:center;line-height:.95}
.effortless .l1{font-size:40px;color:var(--orange)}
.effortless .l2{font-size:40px;color:var(--blue)}
.certificate{left:100px;top:640px;width:54px;height:76px;border-radius:3px;
  background:linear-gradient(150deg,#f3cf59,#c98f12)}
.visit{left:370px;top:722px;width:160px;text-align:center;font-size:10px;line-height:1.35;color:var(--ink)}

/* back */
.set-up{left:60px;top:36px;width:300px;text-align:center;line-height:.95}
.set-up .l1{font-size:40px;color:var(--red)}
.set-up .l2{font-size:40px;color:var(--blue)}
.photo--gamers{left:370px;top:40px;width:200px;height:200px;
  background:radial-gradient(circle at 45% 45%,#e6c4a8,#9a7358 55%,#3f5b6e);
  box-shadow:0 0 0 12px var(--orange)}
.builds{left:20px;top:130px;width:340px;text-align:center;font-size:16px;line-height:1.25}
.how{left:50px;top:190px;font-size:25px;color:var(--red)}
.steps{list-style:none;left:24px;top:234px;width:470px;font-size:10.5px;line-height:1.4;color:var(--muted)}
.steps li{margin-bottom:7px}
.games-head{left:100px;top:362px;width:260px;text-align:center;line-height:.95}
.games-head .l1{font-size:33px;color:var(--red)}
.games-head .l2{font-size:22px;color:var(--blue)}
.games-head .l3{font-size:32px;color:var(--blue)}
.game{position:absolute;width:70px;height:70px;border-radius:50%}
.game--1{left:70px;top:478px;background:radial-gradient(circle,#3b62d6,var(--game-deep))}
.game--2{left:150px;top:470px;background:radial-gradient(circle,#c77a2c,#1b3c8e)}
.game--3{left:230px;top:482px;background:radial-gradient(circle,#6fc83a,#245c1c)}
.game--4{left:310px;top:500px;background:radial-gradient(circle,#2a4fa8,#0b1436)}
.game--5{left:80px;top:560px;background:radial-gradient(circle,#4a8fe0,#13286a)}
.game--6{left:160px;top:560px;background:radial-gradient(circle,#28407f,#070d26)}
.game--7{left:250px;top:576px;background:radial-gradient(circle,#4a4a4a,#111)}
.call{left:90px;top:644px;line-height:.95;color:var(--red)}
.call .l1{font-size:30px}.call .l2{font-size:30px}
.helper{left:280px;top:714px;display:flex;align-items:center;gap:6px;font-size:14px;color:var(--ink)}
.helper-mark{width:26px;height:26px;border-radius:50%;background:var(--ink)}
</style>
</head>
<body>

<section class="page page--front" aria-label="Brochure front">
  <svg class="layer" viewBox="0 0 540 764" aria-hidden="true">
    <path d="M10 395 C80 395 120 370 150 365 S240 330 285 320 S420 260 540 245" fill="none" stroke="var(--sky)" stroke-width="50" stroke-linecap="round"/>
    <circle cx="490" cy="250" r="108" fill="var(--sky)"/>
    <circle cx="285" cy="320" r="92" fill="var(--sky)"/>
    <circle cx="150" cy="365" r="64" fill="var(--sky)"/>
    <path d="M0 764 V730 Q20 700 55 707 Q80 685 115 700 Q150 695 160 725 Q200 700 240 715 Q270 707 280 735 V764 Z" fill="var(--red)"/>
    <path d="M150 764 Q160 730 195 728 Q220 708 255 722 Q285 715 295 745 V764 Z" fill="var(--blue)"/>
    <path d="M330 764 Q335 725 370 723 Q390 698 430 705 Q460 688 490 703 Q530 702 540 722 V764 Z" fill="var(--green)"/>
  </svg>

  <div class="abs title-maths display"><span class="c-red">M</span><span class="c-blue">a</span><span class="c-green">t</span><span class="c-orange">h</span><span class="c-purple">s</span></div>
  <div class="abs title-challenge display"><span class="c-blue">Ch</span><span class="c-green">al</span><span class="c-orange">le</span><span class="c-purple">ng</span><span class="c-red">e</span></div>
  <div class="abs title-fundraiser display">FUNDRAISER</div>

  <div class="abs brand display"><span class="brand-dot"></span><span>Bright Quest<br>Appeal</span></div>

  <p class="abs tagline">A great fundraiser helping primary school students with maths!</p>

  <div class="photo photo--classroom" role="img" aria-label="Photo of smiling students using laptops in a classroom"></div>
  <div class="photo photo--cheer" role="img" aria-label="Photo of a child cheering at home with a laptop"></div>

  <div class="abs challenge-badge">
    <div class="big display">Students</div>
    <div class="mid display">love a challenge!</div>
    <p class="small">Students are challenged to solve educational maths games on the Bright Quest Appeal website.</p>
  </div>

  <div class="abs free-badge display">FREE<br>TO<br>JOIN</div>

  <div class="abs fun-head display"><div class="l1">It's lots of fun and helps</div><div class="l2">students with maths</div></div>

  <ul class="abs ticks ticks--left">
    <li><svg viewBox="0 0 16 14"><path d="M1 7 L6 12 L15 1" fill="none" stroke="var(--red)" stroke-width="2.5"/></svg>The maths challenge is designed to build confidence in mathematics for primary school students.</li>
    <li><svg viewBox="0 0 16 14"><path d="M1 7 L6 12 L15 1" fill="none" stroke="var(--purple)" stroke-width="2.5"/></svg>Once students have completed their maths challenge, they may download a certificate of congratulations.</li>
  </ul>

  <div class="abs certificate" role="img" aria-label="Certificate badge"></div>

  <div class="abs effortless display"><div class="l1">Effortless</div><div class="l2">to run!</div></div>

  <ul class="abs ticks ticks--right">
    <li><svg viewBox="0 0 16 14"><path d="M1 7 L6 12 L15 1" fill="none" stroke="var(--red)" stroke-width="2.5"/></svg>It's all set-up online and ready to go. No spending time or effort planning activities or fundraiser days.</li>
    <li><svg viewBox="0 0 16 14"><path d="M1 7 L6 12 L15 1" fill="none" stroke="var(--red)" stroke-width="2.5"/></svg>The Bright Quest Appeal website is fully safe and secure with no information sharing, no links to other sites and no popup advertising.</li>
    <li><svg viewBox="0 0 16 14"><path d="M1 7 L6 12 L15 1" fill="none" stroke="var(--purple)" stroke-width="2.5"/></svg>Plus, all Bright Quest Appeal games are aligned with the Australian Mathematics Curriculum.</li>
  </ul>

  <p class="abs visit">visit us<br>www.brightquestappeal.example</p>
</section>

<section class="page page--back" aria-label="Brochure back">
  <svg class="layer" viewBox="0 0 540 764" aria-hidden="true">
    <path d="M0 764 V690 Q30 660 70 675 Q100 650 140 672 Q170 670 180 700 Q200 690 215 715 V764 Z" fill="var(--green)"/>
    <path d="M180 764 Q190 720 240 718 Q270 690 320 705 Q360 690 390 715 Q440 705 450 740 Q500 730 540 745 V764 Z" fill="#ffffff"/>
  </svg>

  <div class="abs set-up display"><div class="l1">All set up</div><div class="l2">online for you</div></div>
  <div class="photo photo--gamers" role="img" aria-label="Photo of two excited children playing games on a laptop"></div>
  <p class="abs builds">Builds confidence in maths for students!<br>Easy to run!</p>

  <div class="abs how display">Here is how <span class="c-green">it works</span></div>
  <ol class="abs steps">
    <li>1. Let us know how many memberships you need for your Bright Quest Appeal.</li>
    <li>2. We will send you our website access code for these memberships.</li>
    <li>3. Download our fundraising letter, photocopy and give to parents to collect funds. (See our website for details.)</li>
    <li>4. On our website, each year level has a set of maths challenges for students to solve. Completed students may download a certificate of congratulations.</li>
  </ol>

  <div class="abs games-head display"><div class="l1">Over 260 maths</div><div class="l2">games for foundation</div><div class="l3">to Grade 6</div></div>

  <svg class="abs" style="left:370px;top:418px" width="64" height="56" viewBox="0 0 64 56" aria-hidden="true">
    <rect x="20" y="2" width="20" height="18" rx="4" fill="var(--green)"/>
    <text x="30" y="16" text-anchor="middle" font-family="Open Sans, sans-serif" font-size="12" font-weight="700" fill="var(--blue)">3</text>
    <rect x="2" y="24" width="20" height="18" rx="4" fill="#5db7e8"/>
    <text x="12" y="38" text-anchor="middle" font-family="Open Sans, sans-serif" font-size="12" font-weight="700" fill="#fff">1</text>
    <rect x="30" y="20" width="20" height="18" rx="4" fill="#ef5b7c"/>
    <text x="40" y="34" text-anchor="middle" font-family="Open Sans, sans-serif" font-size="12" font-weight="700" fill="#fff">2</text>
  </svg>

  <div class="game game--1" role="img" aria-label="Game 1 screenshot, Preschool level"></div>
  <div class="game game--2" role="img" aria-label="Game 2 screenshot"></div>
  <div class="game game--3" role="img" aria-label="Game 3 screenshot"></div>
  <div class="game game--4" role="img" aria-label="Game 4 screenshot"></div>
  <div class="game game--5" role="img" aria-label="Game 5 screenshot"></div>
  <div class="game game--6" role="img" aria-label="Game 6 screenshot"></div>
  <div class="game game--7" role="img" aria-label="Game 7 screenshot, Grade 6 level"></div>

  <svg class="abs" style="left:38px;top:648px" width="44" height="44" viewBox="0 0 44 44" aria-hidden="true">
    <path d="M12 8 C8 10 6 16 10 24 C14 32 22 38 28 36 L32 32 L26 26 L22 28 C19 26 16 22 15 19 L18 15 L14 8 Z" fill="none" stroke="var(--green)" stroke-width="2.5" stroke-linejoin="round"/>
    <path d="M30 10 A8 8 0 0 1 34 18 M33 5 A14 14 0 0 1 40 18" fill="none" stroke="var(--green)" stroke-width="2.5" stroke-linecap="round"/>
  </svg>
  <div class="abs call display"><div class="l1">Call for more</div><div class="l2">1300 000 555</div></div>

  <div class="abs helper display"><span class="helper-mark"></span><span>Funds Helper Co</span></div>
</section>

</body>
</html>
```